Harborlight Capital Estates business card

We are a real estate advisory and investment company. We are specialized in assisting high networth individuals to invest in real estate overseas. We deliver a very personalized service, anticipating all the potential challenges an investor can face, and making it easy and safe for them. We also co-invest with our clients, assuring them that each project will be looked after as it is our own, and at the same time giving them the extra booth on confidence to invest.

We need a business card design. The business card must have a very premium, high-end look, reflecting principles like "commitment", "trust" and "timeless (but contemporary)". We look for long term relationships with our clients, and we grow with their referrals. We are all about conquering the confidence of the clients by always delivering above the expectations performance.

Target Market(s)

High net worth individuals.

Industry/Entity Type

Real Estate

Contact Information for Business Card

Please consider places on the business card for:

Name
Function (bellow name in smaller size text)

Mobile phone
E-mail
Skype ID
WeChat ID

Adress (3 lines)

Also include the following locations references:
PORTUGAL * DUBAI * HONG KONG

Website: www.hcestates-example.com

Requirements
Must have
• Company Logo

```html
<!DOCTYPE html>
<html lang="en">
<head>
<meta charset="utf-8">
<title>Harborlight Capital Estates – Business Card</title>
<link rel="stylesheet" href="https://fonts.googleapis.com/css2?family=Open+Sans:wght@400;600&display=swap">
<style>
  :root {
    --page-bg: #e9ebee;
    --card-bg: #ffffff;
    --card-edge: #d6dadf;
    --brand-blue: #1f86cc;
    --band-blue: #1d80c3;
    --band-text: #e3edf6;
    --ink: #3a3d41;
    --divider: #8e9399;
  }
  * { margin: 0; padding: 0; box-sizing: border-box; }
  html, body {
    width: 1200px; height: 970px; overflow: hidden;
    background: var(--page-bg);
    font-family: "Open Sans", Arial, sans-serif;
  }
  .card {
    position: absolute; left: 100px; top: 206px;
    width: 1000px; height: 557px;
    background: var(--card-bg);
    border: 1px solid var(--card-edge);
    box-shadow: 0 10px 30px rgba(0,0,0,0.08);
    overflow: hidden;
  }
  .brand {
    position: absolute; left: 50px; top: 214px; width: 438px;
    display: flex; align-items: center; gap: 16px;
  }
  .brand-dot {
    flex: 0 0 auto; width: 40px; height: 40px; border-radius: 50%;
    background: var(--brand-blue);
  }
  .brand-name {
    color: var(--brand-blue); font-weight: 600;
    font-size: 33px; line-height: 1.15; letter-spacing: 0.5px;
  }
  .divider {
    position: absolute; left: 538px; top: 115px;
    width: 2px; height: 325px; background: var(--divider);
  }
  .details {
    position: absolute; left: 591px; top: 102px;
    color: var(--ink);
  }
  .person-name { color: var(--brand-blue); font-size: 27px; font-weight: 600; line-height: 32px; }
  .person-role { font-size: 22px; line-height: 28px; }
  .address { margin-top: 32px; font-size: 22px; line-height: 29px; }
  .contacts { margin-top: 26px; list-style: none; font-size: 22px; line-height: 31px; }
  .contacts li { display: flex; align-items: center; gap: 8px; }
  .contacts svg { width: 20px; height: 20px; flex: 0 0 auto; fill: var(--brand-blue); }
  .locations {
    position: absolute; left: 0; bottom: 0; width: 100%; height: 45px;
    background: var(--band-blue); color: var(--band-text);
    display: flex; align-items: center; justify-content: center;
    font-size: 20px; letter-spacing: 7px; word-spacing: 16px;
  }
</style>
</head>
<body>
  <div class="card">
    <div class="brand">
      <span class="brand-dot"></span>
      <span class="brand-name">Harborlight<br>Capital Estates</span>
    </div>

    <div class="divider"></div>

    <div class="details">
      <div class="person-name">Daniel Moreton</div>
      <div class="person-role">Manager</div>
      <div class="address">
        4120 Linden Park Ave<br>
        Suite 210<br>
        Easton, Maryland 21601
      </div>
      <ul class="contacts">
        <li><svg viewBox="0 0 20 20"><circle cx="10" cy="10" r="8"/></svg>hcestates</li>
        <li><svg viewBox="0 0 20 20"><circle cx="10" cy="10" r="8"/></svg>hcestates</li>
        <li><svg viewBox="0 0 20 20"><path d="M3 13c0-5 3-8 7-8s7 3 7 8l-3 0-1-3H7l-1 3z M5 14h10v3H5z"/></svg>000 000 000</li>
        <li><svg viewBox="0 0 20 20"><path d="M2 5h16v10H2z" fill="none" stroke="#1f86cc" stroke-width="0"/><path d="M2 5h16l-8 6z"/><path d="M2 7l8 6 8-6v9H2z"/></svg>info@hcestates-example.com</li>
        <li><svg viewBox="0 0 20 20"><circle cx="10" cy="10" r="7.5" fill="none" stroke="#1f86cc" stroke-width="2"/><path d="M2.5 10h15M10 2.5c-3 3-3 12 0 15M10 2.5c3 3 3 12 0 15" fill="none" stroke="#1f86cc" stroke-width="1.5"/></svg>www.hcestates-example.com</li>
      </ul>
    </div>

    <div class="locations">PORTUGAL - DUBAI - HONG KONG</div>
  </div>
</body>
</html>
```